Vorette Business Card

We need a business card design for Vorette, an independent sewing pattern company based near Quebec City. We make patterns for children and adults and specialize in everything other big pattern brands won't tackle: activewear, sportswear (figure skating, gymnastics), underwear. We are a small business and would like our cards to be stylish and fun, not corporate looking.

Target Market(s)

Educated women 35-55 who sew for themselves or their family. They like fashion and sew to be different and make clothes that fit them like a glove, not necessarily to save money.

Industry/Entity Type

Small Business

Requirements
Must have
• Vorette logo, contact info:

Claire Dufresne, president & founder / présidente et fondatrice

Vorette
1635 rue Gosselin
St-Apollinaire QC G0S2E0
Canada

info@vorette.com
www.vorette.com
Nice to have
• Sewing/fashion-related graphics. You can use any pattern cover available on www.vorette.com for inspiration. Stylish illustrations / sketches inspired by existing garments we have would be great. Something showing pattern grading could also be an option.

The design can be on one- or two-sided. We are open to variations (e.g. 4-5 different backs for a given card)
Should not have
• nothing too cartoonish or girly please :) we prefer something timeless, fashion-forward.

```html
<!DOCTYPE html>
<html lang="en">
<head>
<meta charset="utf-8">
<title>Vorette Business Card</title>
<link href="https://fonts.googleapis.com/css2?family=Open+Sans:wght@400;600;700&display=swap" rel="stylesheet">
<style>
  :root {
    --page: #e6e4e1;
    --card-white: #ffffff;
    --card-black: #0d0d0e;
    --ink: #1c1c1c;
    --ink-soft: #3a3a3a;
    --band-light: #f0f0f2;
    --band-dark: #2a2b2d;
    --paper-white: #ffffff;
  }
  * { margin: 0; padding: 0; box-sizing: border-box; }
  html, body { width: 1200px; height: 1024px; overflow: hidden; }
  body {
    background: var(--page);
    font-family: "Open Sans", Arial, sans-serif;
    color: var(--ink);
    position: relative;
  }
  .card {
    position: absolute;
    left: 280px;
    width: 640px;
    height: 366px;
    border-radius: 28px;
    overflow: hidden;
    box-shadow: 0 10px 30px rgba(0,0,0,0.18);
  }
  .card-front { top: 116px; background: var(--card-white); }
  .card-back { top: 542px; background: var(--card-black); }
  .card-decor { position: absolute; inset: 0; width: 100%; height: 100%; }

  .brand-name {
    position: absolute;
    font-weight: 700;
    font-size: 44px;
    letter-spacing: 0.5px;
    line-height: 1;
  }
  .card-front .brand-name { left: 48px; top: 150px; color: var(--ink); }
  .card-back .brand-name { right: 70px; bottom: 70px; color: var(--paper-white); }

  .holder {
    position: absolute;
    left: 250px;
    bottom: 48px;
  }
  .holder-name { font-size: 24px; font-weight: 700; color: var(--ink-soft); }
  .holder-title { font-size: 20px; font-weight: 400; color: var(--ink-soft); margin-top: 2px; }

  .contact {
    position: absolute;
    left: 400px;
    top: 62px;
    list-style: none;
    font-size: 18px;
    line-height: 30px;
    color: var(--ink);
  }
  .contact li { display: flex; align-items: center; gap: 10px; }
  .contact .icon { width: 16px; height: 16px; flex: none; fill: var(--ink); }
  .contact .address { padding-left: 26px; }
</style>
</head>
<body>

<section class="card card-front" aria-label="Business card front">
  <svg class="card-decor" viewBox="0 0 640 366" aria-hidden="true">
    <path d="M330 0 H420 C360 120 300 250 270 366 H170 C210 250 270 120 330 0 Z" fill="var(--band-light)"/>
    <path d="M240 0 H640 V40 C520 48 400 44 300 30 Z" fill="var(--band-light)" opacity="0.7"/>
  </svg>

  <div class="brand-name">Vorette</div>

  <div class="holder">
    <div class="holder-name">Claire Dufresne</div>
    <div class="holder-title">president / présidente</div>
  </div>

  <ul class="contact">
    <li>
      <svg class="icon" viewBox="0 0 16 16"><path d="M3.5 1.5 6 4 4.6 5.6c.8 1.9 2.1 3.2 4 4L10 8.2l2.5 2.5-1.6 2.2C6 12.5 3 9.5 1.8 4.6Z"/></svg>
      418-555-0163
    </li>
    <li>
      <svg class="icon" viewBox="0 0 16 16"><path d="M1 3h14v10H1Zm1.5 1.5v.4L8 8.6l5.5-3.7v-.4Z"/></svg>
      info@vorette.com
    </li>
    <li>
      <svg class="icon" viewBox="0 0 16 16"><circle cx="8" cy="8" r="7"/><path d="M1 8h14M8 1c-3 3.5-3 10.5 0 14M8 1c3 3.5 3 10.5 0 14" stroke="#fff" stroke-width="1" fill="none"/></svg>
      www.vorette.com
    </li>
    <li class="address">1635 rue Gosselin</li>
    <li class="address">St-Apollinaire QC G0S2E0</li>
  </ul>
</section>

<section class="card card-back" aria-label="Business card back">
  <svg class="card-decor" viewBox="0 0 640 366" aria-hidden="true">
    <defs>
      <linearGradient id="back-sheen" x1="0" y1="0" x2="1" y2="1">
        <stop offset="0" stop-color="#1b1c1e"/>
        <stop offset="1" stop-color="#0a0a0b"/>
      </linearGradient>
    </defs>
    <rect width="640" height="366" fill="url(#back-sheen)"/>
    <path d="M250 0 H300 L120 366 H70 Z" fill="var(--band-dark)" opacity="0.8"/>
    <line x1="380" y1="310" x2="580" y2="310" stroke="var(--paper-white)" stroke-width="2"/>
  </svg>
  <div class="brand-name">Vorette</div>
</section>

</body>
</html>
```